Modern & Simple Essential Oils Label

Company Name: Meadowlark Essentials

What we sell: Aromatherapy products, pure therapeutic essential oils.

Design need:
We are looking for a creative and youthful design for the labels used on small essentials oils.

I have two sizes of bottles that I use for essential oils a 5ml bottle and a 15ml bottle. They are dark Amber color glass with black lids. I like the clear labels or mayble a dark brown background. With white or clear lettering with punch of color too! Each oil type is represented by different color. (lavender- purple, lemon - yellow). The label will be the same for all the oils in the two sizes with only a different oil name & coordinating color.
5ml label size should be: 1 " x 2.625"
15ml label size should be: 1.5" x 3.5"

I have some labels that I have had another designer start on, but they aren't quite what I want and missing that something (alot!).. I don't know what. Interest maybe? Lack of design? I dunno.. they are attached. Maybe it's the logo? I don't know! But its gotta change! When I cut out a proof and put a sample on the bottle as I look straight on at the label all I see is a big dot, no logo.. nothing interesting.
Updates

Project Deadline Extended
Reason: Hi! Id like to extend this deadline. Ive been unavailable for a few days due to an illness and Im so far behind! Im feeling MUCH better and looking forward to getting caught up and move with the project. Im not sure how this works, but I attached a list of the oils that we currently have available. And in the list is the idea for the color schemes for the oils. The basic idea is for it to have a wide array of colors, so using different shades of greens, yellows, oranges and so on. So that its like a rainbow. We are not set of that particular color for that particular oil. It was just a idea list of possible colors for oils. Thanks so much!

Target Market(s)

Metro & Modern people. Interested in healthy organic living, Mostly women (some men) 20-45 who are interested in holistic healing.

Industry/Entity Type

It Company

Requirements
Must have
• A reputable look. Clean, organic, crisp, zen or spa-like feel. Modern, youthful appealing label design. Approachable and interesting, not intimidating so that I don't turn away people who are new or not familiar with how to use essential oils.
Should not have
• do NOT want the look to be anywhere close to medicinal, witchy, crafty, hippie, mystical, overly earthy, magical, or voodoo. Do not want it to look like something out of a grandmothers medicine cabinet.

```html
<!DOCTYPE html>
<html lang="en">
<head>
<meta charset="utf-8">
<title>Meadowlark Essentials – 15 ml Essential Oil Labels</title>
<link href="https://fonts.googleapis.com/css2?family=Roboto+Condensed:ital,wght@0,400;0,700;1,400&family=Yellowtail&display=swap" rel="stylesheet">
<style>
  :root{
    --paper:#ffffff;
    --panel:#ebe9e6;
    --ink:#7a7773;
    --ink-strong:#55524e;
    --crop:#8a8a8a;
    --white:#ffffff;
  }
  html,body{margin:0;padding:0;overflow:hidden;}
  body{width:1200px;height:849px;background:var(--paper);position:relative;
       font-family:"Roboto Condensed",Arial,sans-serif;}

  .oil-cassia{--oil:#e08a12;}
  .oil-clove{--oil:#c4900f;}
  .oil-euc-radiata{--oil:#6b7a58;}
  .oil-basil{--oil:#6db832;}
  .oil-cedarwood{--oil:#8f7340;}
  .oil-coffee{--oil:#7c4e1c;}
  .oil-fennel{--oil:#7b8069;}
  .oil-bergamot{--oil:#a6c30f;}
  .oil-chamomile{--oil:#9a7b62;}
  .oil-coriander{--oil:#6a9e35;}
  .oil-fir{--oil:#8d8f82;}
  .oil-camphor{--oil:#76b32e;}
  .oil-cinnamon{--oil:#e25219;}
  .oil-cypress{--oil:#386a2f;}
  .oil-frankincense{--oil:#f28a30;}
  .oil-carrot{--oil:#f4a000;}
  .oil-clary{--oil:#e8609a;}
  .oil-euc-globulus{--oil:#5e6e44;}
  .oil-geranium{--oil:#e9609c;}

  .label{position:absolute;width:256px;height:112px;display:flex;}
  .label::before,.label::after{content:"";position:absolute;left:128px;width:1px;height:10px;background:var(--crop);}
  .label::before{top:-12px;}
  .label::after{bottom:-12px;}

  /* back panel: text reads bottom-to-top */
  .label-back{position:relative;width:128px;height:112px;background:var(--panel);overflow:hidden;}
  .back-content{position:absolute;width:104px;height:116px;left:12px;top:-2px;transform:rotate(-90deg);
       color:var(--ink);font-size:4.6px;line-height:1.3;}
  .facts{border:0.6px solid var(--ink);margin-bottom:6px;}
  .facts-body{padding:2px 3px;}
  .facts-title{font-weight:700;font-size:6px;color:var(--ink-strong);margin-bottom:1px;}
  .grade{background:var(--oil);color:var(--white);font-size:4.4px;line-height:6px;padding:0 3px;}
  .company p{margin:0 0 3px;}
  .caution b{color:var(--ink-strong);}

  /* front panel */
  .label-front{position:relative;width:128px;height:112px;background:var(--oil);color:var(--white);overflow:hidden;}
  .latin{position:absolute;left:80px;top:8px;font-style:italic;font-size:4.8px;line-height:1.25;text-transform:uppercase;}
  .oil-name{position:absolute;left:6px;top:26px;width:116px;height:62px;
       display:flex;flex-direction:column;justify-content:center;
       font-family:"Yellowtail",cursive;font-size:29px;line-height:0.85;
       transform:rotate(-6deg);white-space:nowrap;}
  .oil-name .second{padding-left:16px;}
  .oil-name.two{font-size:27px;}
  .oil-name.long{font-size:21px;}
  .oil-name small{font-size:12px;padding-left:4px;}
  .brand-bar{position:absolute;left:0;right:0;bottom:0;height:22px;border-top:1px solid var(--white);display:flex;align-items:center;}
  .volume{width:14px;height:100%;border-right:1px solid var(--white);display:flex;align-items:center;justify-content:center;}
  .volume span{display:block;transform:rotate(-90deg);white-space:nowrap;font-size:6.5px;font-weight:700;}
  .brand{padding-left:8px;font-size:10px;font-weight:400;white-space:nowrap;}
</style>
</head>
<body>
<main class="sheet">

<!-- row 1 -->
<article class="label oil-cassia" style="left:313px;top:35px">
  <div class="label-back"><div class="back-content">
    <div class="facts"><div class="facts-body"><div class="facts-title">Supplemental Facts</div>Serving Size: 1 drop<br>Servings Per Container: About 250<br>Oil: Cinnamomum Cassia</div><div class="grade">100% Pure Therapeutic Grade</div></div>
    <div class="company"><p>Meadowlark Essentials<br>P.O. Box 402, Fairbrook, UT 84900</p><p>For aromatic, topical or dietary use. 100% pure therapeutic-grade essential oil. Dilute with a carrier oil before using.</p><p class="caution"><b>CAUTION:</b> Possible skin sensitivity. Keep out of reach of children. If pregnant or under a doctor's care, consult your physician.</p></div>
  </div></div>
  <div class="label-front"><div class="latin">Cinnamomum<br>Cassia<br>100% Pure<br>Essential Oil</div><div class="oil-name">Cassia</div><div class="brand-bar"><div class="volume"><span>15 ml</span></div><div class="brand">Meadowlark Essentials</div></div></div>
</article>

<article class="label oil-clove" style="left:613px;top:35px">
  <div class="label-back"><div class="back-content">
    <div class="facts"><div class="facts-body"><div class="facts-title">Supplemental Facts</div>Serving Size: 1 drop<br>Servings Per Container: About 250<br>Oil: Syzygium Aromaticum</div><div class="grade">100% Pure Therapeutic Grade</div></div>
    <div class="company"><p>Meadowlark Essentials<br>P.O. Box 402, Fairbrook, UT 84900</p><p>For aromatic, topical or dietary use. 100% pure therapeutic-grade essential oil. Dilute with a carrier oil before using.</p><p class="caution"><b>CAUTION:</b> Possible skin sensitivity. Keep out of reach of children. If pregnant or under a doctor's care, consult your physician.</p></div>
  </div></div>
  <div class="label-front"><div class="latin">Syzygium<br>Aromaticum<br>100% Pure<br>Essential Oil</div><div class="oil-name two"><span>Clove</span><span class="second">bud</span></div><div class="brand-bar"><div class="volume"><span>15 ml</span></div><div class="brand">Meadowlark Essentials</div></div></div>
</article>

<article class="label oil-euc-radiata" style="left:900px;top:35px">
  <div class="label-back"><div class="back-content">
    <div class="facts"><div class="facts-body"><div class="facts-title">Supplemental Facts</div>Serving Size: 1 drop<br>Servings Per Container: About 250<br>Oil: Eucalyptus Radiata</div><div class="grade">100% Pure Therapeutic Grade</div></div>
    <div class="company"><p>Meadowlark Essentials<br>P.O. Box 402, Fairbrook, UT 84900</p><p>For aromatic, topical or dietary use. 100% pure therapeutic-grade essential oil. Dilute with a carrier oil before using.</p><p class="caution"><b>CAUTION:</b> Possible skin sensitivity. Keep out of reach of children. If pregnant or under a doctor's care, consult your physician.</p></div>
  </div></div>
  <div class="label-front"><div class="latin">Eucalyptus<br>Radiata<br>100% Pure<br>Essential Oil</div><div class="oil-name long"><span>Eucalyptus</span><span class="second">Radiata</span></div><div class="brand-bar"><div class="volume"><span>15 ml</span></div><div class="brand">Meadowlark Essentials</div></div></div>
</article>

<!-- row 2 -->
<article class="label oil-basil" style="left:27px;top:202px">
  <div class="label-back"><div class="back-content">
    <div class="facts"><div class="facts-body"><div class="facts-title">Supplemental Facts</div>Serving Size: 1 drop<br>Servings Per Container: About 250<br>Oil: Ocimum Basilicum</div><div class="grade">100% Pure Therapeutic Grade</div></div>
    <div class="company"><p>Meadowlark Essentials<br>P.O. Box 402, Fairbrook, UT 84900</p><p>For aromatic, topical or dietary use. 100% pure therapeutic-grade essential oil. Dilute with a carrier oil before using.</p><p class="caution"><b>CAUTION:</b> Possible skin sensitivity. Keep out of reach of children. If pregnant or under a doctor's care, consult your physician.</p></div>
  </div></div>
  <div class="label-front"><div class="latin">Ocimum<br>Basilicum<br>100% Pure<br>Essential Oil</div><div class="oil-name">Basil</div><div class="brand-bar"><div class="volume"><span>15 ml</span></div><div class="brand">Meadowlark Essentials</div></div></div>
</article>

<article class="label oil-cedarwood" style="left:313px;top:202px">
  <div class="label-back"><div class="back-content">
    <div class="facts"><div class="facts-body"><div class="facts-title">Supplemental Facts</div>Serving Size: 1 drop<br>Servings Per Container: About 250<br>Oil: Cedrus Atlantica</div><div class="grade">100% Pure Therapeutic Grade</div></div>
    <div class="company"><p>Meadowlark Essentials<br>P.O. Box 402, Fairbrook, UT 84900</p><p>For aromatic, topical or dietary use. 100% pure therapeutic-grade essential oil. Dilute with a carrier oil before using.</p><p class="caution"><b>CAUTION:</b> Possible skin sensitivity. Keep out of reach of children. If pregnant or under a doctor's care, consult your physician.</p></div>
  </div></div>
  <div class="label-front"><div class="latin">Cedrus<br>Atlantica<br>100% Pure<br>Essential Oil</div><div class="oil-name two"><span>Cedar</span><span class="second">wood</span></div><div class="brand-bar"><div class="volume"><span>15 ml</span></div><div class="brand">Meadowlark Essentials</div></div></div>
</article>

<article class="label oil-coffee" style="left:613px;top:202px">
  <div class="label-back"><div class="back-content">
    <div class="facts"><div class="facts-body"><div class="facts-title">Supplemental Facts</div>Serving Size: 1 drop<br>Servings Per Container: About 250<br>Oil: Coffea Arabica</div><div class="grade">100% Pure Therapeutic Grade</div></div>
    <div class="company"><p>Meadowlark Essentials<br>P.O. Box 402, Fairbrook, UT 84900</p><p>For aromatic, topical or dietary use. 100% pure therapeutic-grade essential oil. Dilute with a carrier oil before using.</p><p class="caution"><b>CAUTION:</b> Possible skin sensitivity. Keep out of reach of children. If pregnant or under a doctor's care, consult your physician.</p></div>
  </div></div>
  <div class="label-front"><div class="latin">Coffea<br>Arabica<br>100% Pure<br>Essential Oil</div><div class="oil-name">Coffee</div><div class="brand-bar"><div class="volume"><span>15 ml</span></div><div class="brand">Meadowlark Essentials</div></div></div>
</article>

<article class="label oil-fennel" style="left:900px;top:202px">
  <div class="label-back"><div class="back-content">
    <div class="facts"><div class="facts-body"><div class="facts-title">Supplemental Facts</div>Serving Size: 1 drop<br>Servings Per Container: About 250<br>Oil: Foeniculum Vulgare</div><div class="grade">100% Pure Therapeutic Grade</div></div>
    <div class="company"><p>Meadowlark Essentials<br>P.O. Box 402, Fairbrook, UT 84900</p><p>For aromatic, topical or dietary use. 100% pure therapeutic-grade essential oil. Dilute with a carrier oil before using.</p><p class="caution"><b>CAUTION:</b> Possible skin sensitivity. Keep out of reach of children. If pregnant or under a doctor's care, consult your physician.</p></div>
  </div></div>
  <div class="label-front"><div class="latin">Foeniculum<br>Vulgare<br>100% Pure<br>Essential Oil</div><div class="oil-name">Funnel</div><div class="brand-bar"><div class="volume"><span>15 ml</span></div><div class="brand">Meadowlark Essentials</div></div></div>
</article>

<!-- row 3 -->
<article class="label oil-bergamot" style="left:27px;top:368px">
  <div class="label-back"><div class="back-content">
    <div class="facts"><div class="facts-body"><div class="facts-title">Supplemental Facts</div>Serving Size: 1 drop<br>Servings Per Container: About 250<br>Oil: Rosmarinus Officinalis</div><div class="grade">100% Pure Therapeutic Grade</div></div>
    <div class="company"><p>Meadowlark Essentials<br>P.O. Box 402, Fairbrook, UT 84900</p><p>For aromatic, topical or dietary use. 100% pure therapeutic-grade essential oil. Dilute with a carrier oil before using.</p><p class="caution"><b>CAUTION:</b> Possible skin sensitivity. Keep out of reach of children. If pregnant or under a doctor's care, consult your physician.</p></div>
  </div></div>
  <div class="label-front"><div class="latin">Rosmarinus<br>Officinalis<br>100% Pure<br>Essential Oil</div><div class="oil-name two"><span>Berga</span><span class="second">mot</span></div><div class="brand-bar"><div class="volume"><span>15 ml</span></div><div class="brand">Meadowlark Essentials</div></div></div>
</article>

<article class="label oil-chamomile" style="left:313px;top:368px">
  <div class="label-back"><div class="back-content">
    <div class="facts"><div class="facts-body"><div class="facts-title">Supplemental Facts</div>Serving Size: 1 drop<br>Servings Per Container: About 250<br>Oil: Anthemis Nobilis</div><div class="grade">100% Pure Therapeutic Grade</div></div>
    <div class="company"><p>Meadowlark Essentials<br>P.O. Box 402, Fairbrook, UT 84900</p><p>For aromatic, topical or dietary use. 100% pure therapeutic-grade essential oil. Dilute with a carrier oil before using.</p><p class="caution"><b>CAUTION:</b> Possible skin sensitivity. Keep out of reach of children. If pregnant or under a doctor's care, consult your physician.</p></div>
  </div></div>
  <div class="label-front"><div class="latin">Anthemis<br>Nobilis<br>100% Pure<br>Essential Oil</div><div class="oil-name two"><span>Chamo</span><span class="second">mile</span></div><div class="brand-bar"><div class="volume"><span>15 ml</span></div><div class="brand">Meadowlark Essentials</div></div></div>
</article>

<article class="label oil-coriander" style="left:613px;top:368px">
  <div class="label-back"><div class="back-content">
    <div class="facts"><div class="facts-body"><div class="facts-title">Supplemental Facts</div>Serving Size: 1 drop<br>Servings Per Container: About 250<br>Oil: Coriandrum Sativum</div><div class="grade">100% Pure Therapeutic Grade</div></div>
    <div class="company"><p>Meadowlark Essentials<br>P.O. Box 402, Fairbrook, UT 84900</p><p>For aromatic, topical or dietary use. 100% pure therapeutic-grade essential oil. Dilute with a carrier oil before using.</p><p class="caution"><b>CAUTION:</b> Possible skin sensitivity. Keep out of reach of children. If pregnant or under a doctor's care, consult your physician.</p></div>
  </div></div>
  <div class="label-front"><div class="latin">Coriandrum<br>Sativum<br>100% Pure<br>Essential Oil</div><div class="oil-name long" style="font-size:25px">Coriander</div><div class="brand-bar"><div class="volume"><span>15 ml</span></div><div class="brand">Meadowlark Essentials</div></div></div>
</article>

<article class="label oil-fir" style="left:900px;top:368px">
  <div class="label-back"><div class="back-content">
    <div class="facts"><div class="facts-body"><div class="facts-title">Supplemental Facts</div>Serving Size: 1 drop<br>Servings Per Container: About 250<br>Oil: Abies Siberica</div><div class="grade">100% Pure Therapeutic Grade</div></div>
    <div class="company"><p>Meadowlark Essentials<br>P.O. Box 402, Fairbrook, UT 84900</p><p>For aromatic, topical or dietary use. 100% pure therapeutic-grade essential oil. Dilute with a carrier oil before using.</p><p class="caution"><b>CAUTION:</b> Possible skin sensitivity. Keep out of reach of children. If pregnant or under a doctor's care, consult your physician.</p></div>
  </div></div>
  <div class="label-front"><div class="latin">Abies<br>Siberica<br>100% Pure<br>Essential Oil</div><div class="oil-name two"><span>Fir</span><span class="second">Needle</span></div><div class="brand-bar"><div class="volume"><span>15 ml</span></div><div class="brand">Meadowlark Essentials</div></div></div>
</article>

<!-- row 4 -->
<article class="label oil-camphor" style="left:27px;top:535px">
  <div class="label-back"><div class="back-content">
    <div class="facts"><div class="facts-body"><div class="facts-title">Supplemental Facts</div>Serving Size: 1 drop<br>Servings Per Container: About 250<br>Oil: Cinnamomum Camphora</div><div class="grade">100% Pure Therapeutic Grade</div></div>
    <div class="company"><p>Meadowlark Essentials<br>P.O. Box 402, Fairbrook, UT 84900</p><p>For aromatic, topical or dietary use. 100% pure therapeutic-grade essential oil. Dilute with a carrier oil before using.</p><p class="caution"><b>CAUTION:</b> Possible skin sensitivity. Keep out of reach of children. If pregnant or under a doctor's care, consult your physician.</p></div>
  </div></div>
  <div class="label-front"><div class="latin">Cinnamomum<br>Camphora<br>100% Pure<br>Essential Oil</div><div class="oil-name" style="font-size:27px">Camphor</div><div class="brand-bar"><div class="volume"><span>15 ml</span></div><div class="brand">Meadowlark Essentials</div></div></div>
</article>

<article class="label oil-cinnamon" style="left:313px;top:535px">
  <div class="label-back"><div class="back-content">
    <div class="facts"><div class="facts-body"><div class="facts-title">Supplemental Facts</div>Serving Size: 1 drop<br>Servings Per Container: About 250<br>Oil: Cinnamomum Zeylanicum</div><div class="grade">100% Pure Therapeutic Grade</div></div>
    <div class="company"><p>Meadowlark Essentials<br>P.O. Box 402, Fairbrook, UT 84900</p><p>For aromatic, topical or dietary use. 100% pure therapeutic-grade essential oil. Dilute with a carrier oil before using.</p><p class="caution"><b>CAUTION:</b> Possible skin sensitivity. Keep out of reach of children. If pregnant or under a doctor's care, consult your physician.</p></div>
  </div></div>
  <div class="label-front"><div class="latin">Cinnamomum<br>Zeylanicum<br>100% Pure<br>Essential Oil</div><div class="oil-name long"><span>Cinnamon</span><span class="second">Bark</span></div><div class="brand-bar"><div class="volume"><span>15 ml</span></div><div class="brand">Meadowlark Essentials</div></div></div>
</article>

<article class="label oil-cypress" style="left:613px;top:535px">
  <div class="label-back"><div class="back-content">
    <div class="facts"><div class="facts-body"><div class="facts-title">Supplemental Facts</div>Serving Size: 1 drop<br>Servings Per Container: About 250<br>Oil: Cupressus Sempervirens</div><div class="grade">100% Pure Therapeutic Grade</div></div>
    <div class="company"><p>Meadowlark Essentials<br>P.O. Box 402, Fairbrook, UT 84900</p><p>For aromatic, topical or dietary use. 100% pure therapeutic-grade essential oil. Dilute with a carrier oil before using.</p><p class="caution"><b>CAUTION:</b> Possible skin sensitivity. Keep out of reach of children. If pregnant or under a doctor's care, consult your physician.</p></div>
  </div></div>
  <div class="label-front"><div class="latin">Cupressus<br>Sempervirens<br>100% Pure<br>Essential Oil</div><div class="oil-name long"><span>Cypress</span><span class="second">french</span></div><div class="brand-bar"><div class="volume"><span>15 ml</span></div><div class="brand">Meadowlark Essentials</div></div></div>
</article>

<article class="label oil-frankincense" style="left:900px;top:535px">
  <div class="label-back"><div class="back-content">
    <div class="facts"><div class="facts-body"><div class="facts-title">Supplemental Facts</div>Serving Size: 1 drop<br>Servings Per Container: About 250<br>Oil: Boswellia Serrata</div><div class="grade">100% Pure Therapeutic Grade</div></div>
    <div class="company"><p>Meadowlark Essentials<br>P.O. Box 402, Fairbrook, UT 84900</p><p>For aromatic, topical or dietary use. 100% pure therapeutic-grade essential oil. Dilute with a carrier oil before using.</p><p class="caution"><b>CAUTION:</b> Possible skin sensitivity. Keep out of reach of children. If pregnant or under a doctor's care, consult your physician.</p></div>
  </div></div>
  <div class="label-front"><div class="latin">Boswellia<br>Serrata<br>100% Pure<br>Essential Oil</div><div class="oil-name long"><span>Frank</span><span class="second">incense <small>(India)</small></span></div><div class="brand-bar"><div class="volume"><span>15 ml</span></div><div class="brand">Meadowlark Essentials</div></div></div>
</article>

<!-- row 5 -->
<article class="label oil-carrot" style="left:27px;top:702px">
  <div class="label-back"><div class="back-content">
    <div class="facts"><div class="facts-body"><div class="facts-title">Supplemental Facts</div>Serving Size: 1 drop<br>Servings Per Container: About 250<br>Oil: Daucus Carota</div><div class="grade">100% Pure Therapeutic Grade</div></div>
    <div class="company"><p>Meadowlark Essentials<br>P.O. Box 402, Fairbrook, UT 84900</p><p>For aromatic, topical or dietary use. 100% pure therapeutic-grade essential oil. Dilute with a carrier oil before using.</p><p class="caution"><b>CAUTION:</b> Possible skin sensitivity. Keep out of reach of children. If pregnant or under a doctor's care, consult your physician.</p></div>
  </div></div>
  <div class="label-front"><div class="latin">Daucus<br>Carota<br>100% Pure<br>Essential Oil</div><div class="oil-name two"><span>Carrot</span><span class="second">Seed</span></div><div class="brand-bar"><div class="volume"><span>15 ml</span></div><div class="brand">Meadowlark Essentials</div></div></div>
</article>

<article class="label oil-clary" style="left:313px;top:702px">
  <div class="label-back"><div class="back-content">
    <div class="facts"><div class="facts-body"><div class="facts-title">Supplemental Facts</div>Serving Size: 1 drop<br>Servings Per Container: About 250<br>Oil: Salvia Sclarea</div><div class="grade">100% Pure Therapeutic Grade</div></div>
    <div class="company"><p>Meadowlark Essentials<br>P.O. Box 402, Fairbrook, UT 84900</p><p>For aromatic, topical or dietary use. 100% pure therapeutic-grade essential oil. Dilute with a carrier oil before using.</p><p class="caution"><b>CAUTION:</b> Possible skin sensitivity. Keep out of reach of children. If pregnant or under a doctor's care, consult your physician.</p></div>
  </div></div>
  <div class="label-front"><div class="latin">Salvia<br>Sclarea<br>100% Pure<br>Essential Oil</div><div class="oil-name two"><span>Clary</span><span class="second">Sage</span></div><div class="brand-bar"><div class="volume"><span>15 ml</span></div><div class="brand">Meadowlark Essentials</div></div></div>
</article>

<article class="label oil-euc-globulus" style="left:613px;top:702px">
  <div class="label-back"><div class="back-content">
    <div class="facts"><div class="facts-body"><div class="facts-title">Supplemental Facts</div>Serving Size: 1 drop<br>Servings Per Container: About 250<br>Oil: Eucalyptus Globulus</div><div class="grade">100% Pure Therapeutic Grade</div></div>
    <div class="company"><p>Meadowlark Essentials<br>P.O. Box 402, Fairbrook, UT 84900</p><p>For aromatic, topical or dietary use. 100% pure therapeutic-grade essential oil. Dilute with a carrier oil before using.</p><p class="caution"><b>CAUTION:</b> Possible skin sensitivity. Keep out of reach of children. If pregnant or under a doctor's care, consult your physician.</p></div>
  </div></div>
  <div class="label-front"><div class="latin">Eucalyptus<br>Globulus<br>100% Pure<br>Essential Oil</div><div class="oil-name long"><span>Eucalyptus</span><span class="second">Globulus</span></div><div class="brand-bar"><div class="volume"><span>15 ml</span></div><div class="brand">Meadowlark Essentials</div></div></div>
</article>

<article class="label oil-geranium" style="left:900px;top:702px">
  <div class="label-back"><div class="back-content">
    <div class="facts"><div class="facts-body"><div class="facts-title">Supplemental Facts</div>Serving Size: 1 drop<br>Servings Per Container: About 250<br>Oil: Pelargonium Graveolens</div><div class="grade">100% Pure Therapeutic Grade</div></div>
    <div class="company"><p>Meadowlark Essentials<br>P.O. Box 402, Fairbrook, UT 84900</p><p>For aromatic, topical or dietary use. 100% pure therapeutic-grade essential oil. Dilute with a carrier oil before using.</p><p class="caution"><b>CAUTION:</b> Possible skin sensitivity. Keep out of reach of children. If pregnant or under a doctor's care, consult your physician.</p></div>
  </div></div>
  <div class="label-front"><div class="latin">Pelargonium<br>Graveolens<br>100% Pure<br>Essential Oil</div><div class="oil-name long" style="font-size:25px">Geranium</div><div class="brand-bar"><div class="volume"><span>15 ml</span></div><div class="brand">Meadowlark Essentials</div></div></div>
</article>

</main>
</body>
</html>
```